Motor Oil Lubricant Package Labels

We are looking for a logo and label that we can put on our motor oil bottle 1 liter and 5 liter. The name of our motor oil is Corvanta. We want to design our flagship logo for CORVANTA MOTOR OILS and as well as the label that will go on the bottle. We have some drafts that we have come up with attached and would like to see more options. The concept of a timeless motor oil and the endless loop of lubricating oils incorporated in the design. We will have full synthetic motor oil, a synthetic blend motor, ATF III transmission fluid, TRZ-IV transmission fluid. hydraulic oils etc. Examples will be attached
Target Market(s)
Automotive Lubricants and Chemicals
Industry/Entity Type
Automotive
Logo Text
Corvanta Lubricants
Font styles to use
Other font styles liked:
- Let designer choose
Requirements
Must have
- The Corvanta sign incorporated in a very cool way to our name. Our brand needs to stick out
Nice to have
- Automotive lubricant related and colors red, white, and blue incorporated in the design
Should not have
- Images of individuals and or topics not related to automotive lubricants.

```html
<!DOCTYPE html>
<html lang="en">
<head>
<meta charset="utf-8">
<title>Corvanta Motor Oil – 5 Liter Label</title>
<link rel="stylesheet" href="https://fonts.googleapis.com/css2?family=Exo+2:wght@800&family=Barlow:wght@500;600;700&display=swap">
<style>
  :root {
    --bg-light: #fbf5dc;
    --bg-warm: #fcd888;
    --label-navy: #262a45;
    --label-brown: #3a2418;
    --label-dark: #1a1414;
    --gold: #f2b327;
    --orange: #f59a1c;
    --silver: #c9cdd3;
    --white: #ffffff;
  }
  html, body {
    margin: 0;
    width: 1200px;
    height: 900px;
    overflow: hidden;
  }
  body {
    background: radial-gradient(ellipse at 50% 10%, var(--bg-light) 0%, #f4e2ac 40%, var(--bg-warm) 100%);
    font-family: "Barlow", sans-serif;
  }
  .label {
    position: absolute;
    left: 340px;
    top: 62px;
    width: 520px;
    height: 776px;
    border-radius: 20px;
    overflow: hidden;
    background: linear-gradient(160deg, var(--label-navy) 0%, #3b3550 30%, var(--label-brown) 62%, var(--label-dark) 100%);
    box-shadow: 0 10px 30px rgba(90, 60, 10, 0.25);
  }
  .label__wave {
    position: absolute;
    inset: 0;
  }
  .brand-block {
    position: absolute;
    left: 30px;
    top: 170px;
    width: 470px;
    transform: rotate(-38deg);
    transform-origin: center;
    color: var(--white);
  }
  .brand-name {
    font-family: "Exo 2", sans-serif;
    font-weight: 800;
    font-size: 104px;
    line-height: 1;
    color: var(--gold);
    text-align: center;
    letter-spacing: -1px;
  }
  .product-line {
    text-align: right;
    font-weight: 700;
    font-size: 30px;
    color: var(--silver);
    letter-spacing: 1px;
    margin: 4px 18px 0 0;
  }
  .oil-type {
    font-weight: 600;
    font-size: 21px;
    color: var(--orange);
    margin: 18px 0 0 10px;
    letter-spacing: 0.5px;
  }
  .grade-row {
    display: flex;
    align-items: center;
    gap: 10px;
    margin-left: 6px;
  }
  .grade-row__sae {
    font-weight: 700;
    font-size: 20px;
    writing-mode: vertical-rl;
    transform: rotate(180deg);
  }
  .grade-row__grade {
    font-weight: 700;
    font-size: 72px;
    line-height: 1;
  }
  .grade-row__use {
    font-weight: 600;
    font-size: 15px;
    line-height: 1.05;
    color: var(--orange);
  }
  .spec {
    font-weight: 700;
    font-size: 30px;
    color: var(--orange);
    margin-left: 150px;
  }
  .volume {
    position: absolute;
    right: 48px;
    bottom: 46px;
    color: var(--white);
    text-align: left;
    line-height: 1.1;
  }
  .volume__oz { font-size: 22px; font-weight: 500; }
  .volume__liter { font-size: 18px; font-weight: 500; }
  .volume__rule {
    height: 2px;
    background: var(--orange);
    margin: 6px 0;
  }
  .volume__made { font-size: 16px; font-weight: 600; }
  .volume__country { font-size: 34px; font-weight: 600; line-height: 1; }
</style>
</head>
<body>
  <main class="label">
    <svg class="label__wave" viewBox="0 0 520 776" role="img" aria-label="Flowing golden motor oil wave illustration">
      <defs>
        <linearGradient id="waveGold" x1="0" y1="1" x2="1" y2="0">
          <stop offset="0" stop-color="#8a3f08"/>
          <stop offset="0.35" stop-color="#f2a21e"/>
          <stop offset="0.6" stop-color="#ffd860"/>
          <stop offset="1" stop-color="#b8600c"/>
        </linearGradient>
      </defs>
      <path d="M0 776 L0 740 C120 700 190 640 260 560 C330 480 400 360 520 300 L520 420 C440 470 390 560 320 640 C260 710 200 750 150 776 Z" fill="url(#waveGold)" opacity="0.9"/>
    </svg>

    <div class="brand-block">
      <div class="brand-name">Corvanta</div>
      <div class="product-line">MOTOR OIL</div>
      <div class="oil-type">• SYNTHETIC BLEND •</div>
      <div class="grade-row">
        <span class="grade-row__sae">SAE</span>
        <span class="grade-row__grade">5W-30</span>
        <span class="grade-row__use">FOR<br>GASOLINE<br>ENGINES</span>
      </div>
      <div class="spec">API SN •</div>
    </div>

    <div class="volume">
      <div class="volume__oz">169oz</div>
      <div class="volume__liter">5 LITER</div>
      <div class="volume__rule"></div>
      <div class="volume__made">MADE IN</div>
      <div class="volume__country">USA</div>
    </div>
  </main>
</body>
</html>
```